App UI Design: Shopping/E-commerce App

Project :
Develop an UI design & App icon for an E-commerce/Shopping App

About the App/ Target Audience:
This grocery & food shopping app will be used by independent pub, café, restaurant owners to place & manage their purchases of foods and groceries for their catering businesses.

They will use the app to access product catalogues & special promotions, search & buy large quantities of groceries or catering supplies, and the ability to manage and track status of their order.

The HTML5 App’s has been built with a very basic structure. It now needs the visual layer of the UI designed

Note:
The app is tailored for business & catering orders, not retail/supermarket buyers, so the visual needs to look smart & not too casual.
Updates

Reason: Current submissions have not met out expectations. Please use the similar app examples in the PDF as a strong point of reference for the look & feel. Feedback will be given as submissions come in, please feel free to submit initial concepts of 1 or 2 of the pages & we'll provide feedback on whether it is on the right track or not before you do more work. Current submission will also receive feedback in the next few days. We look forward to new submissions!

Target Market(s)

Male & Female. Independent pub, café, restaurant owners buying for their catering businesses. Chefs etc.

Industry/Entity Type

Restaurant

Requirements
Must have
• An overview of elements/pages of the app that needs to be designed are:
(DOWNLOAD a more detailed diagram PDF explanation)

1. Welcome- Log-in Page
2. Homepage – index that links to different function of the app

Products:
3. Promotions page – for products on special for a limited time
4. Catalogue page – access to a range of catalogue

Ways to buy:
5. Basket (Shopping Cart) - tracking items they are buying from the catalogues
6. Templates (Pre-set Shopping list)- Set shopping list that has been preloaded for certain menu
7. Open Order page

My Account:
8. My Account/profile page – Users can check the status of their order, look at past orders, look at their account number & details etc

_______________________________________________________

Icon set- Icons to represent each pages that act as visual cues for easier browsing.

2 Main features that need to be accessible & consistent throughout all pages are:
a) The Navigation Bar –
so the user can quickly find their way back & access to the main functions
b) The Search bar –
whether it drops down when needed, or is featured as a header/footer.
c) Log out button
Nice to have

Things to keep in mind:

The UI design essentially needs to be a customizable template that can easily adapt to any brand/logo with a slight change of the color scheme. As we will later implement our brand & logo onto it.

We’re looking for a clean & clear design that allows for a straight forward easy user experience.

You are free to develop different layout & UI pattern that you feel is the most efficient way the user can walk through the App & make their purchase in no more than 2 or 3 clicks
________________________________________________

Screenshot of Similar Apps for reference are also in the PDF

```html
<!DOCTYPE html>
<html lang="en">
<head>
<meta charset="utf-8">
<title>Catering Supply App – Screen Set</title>
<link rel="stylesheet" href="https://fonts.googleapis.com/css2?family=Arimo:wght@400;700&family=Tinos&display=swap">
<style>
:root{
  --stage:#6b6b6d;
  --head-top:#707074;
  --head-bottom:#3c3c3f;
  --bar-black:#161616;
  --search-band:#2b2b2d;
  --beige:#ebe8dc;
  --tan:#e2d7c0;
  --tan-line:#c9b994;
  --strip:#ddd3bb;
  --red:#e3121a;
  --red-dark:#a8080d;
  --btn-top:#5b5b5f;
  --btn-bottom:#2a2a2c;
  --nav-top:#4b4b4e;
  --nav-bottom:#2e2e30;
  --white:#ffffff;
  --text:#222222;
}
*{box-sizing:border-box;margin:0;padding:0}
html,body{width:1200px;height:861px;overflow:hidden}
body{background:var(--stage);font-family:"Arimo",Arial,sans-serif;color:var(--text);position:relative}
.icon-defs{position:absolute;width:0;height:0}

.screen{position:absolute;width:192px;height:273px;overflow:hidden;display:flex;flex-direction:column;background:var(--beige);box-shadow:0 0 0 1px #000}

/* header */
.app-header{height:42px;flex:none;position:relative;background:linear-gradient(var(--head-top),#58585b 48%,var(--head-bottom) 52%,#343437);color:var(--white)}
.brand{position:absolute;left:50%;top:13px;transform:translateX(-50%);font-size:14px;font-weight:400;letter-spacing:.6px;color:var(--white);white-space:nowrap}
.head-action{position:absolute;top:8px;display:flex;flex-direction:column;align-items:center;font-size:4.5px;color:#cfcfcf;gap:2px}
.head-action svg{width:14px;height:14px}
.head-action.back{left:10px}
.head-action.logout{right:8px}
.welcome .app-header{height:48px}
.welcome .brand{top:15px}

.title-bar{height:10px;flex:none;background:var(--bar-black);color:var(--red);font-size:7px;font-weight:700;text-align:center;line-height:10px;text-transform:uppercase}
.search-band{height:26px;flex:none;background:var(--search-band);display:flex;align-items:center;justify-content:center}
.search-field{width:150px;height:15px;border-radius:8px;background:var(--white);display:flex;align-items:center;padding-left:4px;gap:4px;font-size:6px;color:#444}
.search-field svg{width:9px;height:9px}

.content{flex:1;position:relative;overflow:hidden}

/* bottom nav */
.tab-bar{height:32px;flex:none;display:flex;background:linear-gradient(var(--nav-top),var(--nav-bottom))}
.tab{flex:1;display:flex;flex-direction:column;align-items:center;justify-content:center;gap:2px;font-size:3.6px;color:#c8c8c8;text-transform:uppercase}
.tab svg{width:15px;height:15px}
.tab.active{background:#000;color:var(--white)}

/* menu buttons */
.menu{display:flex;flex-direction:column;align-items:center;gap:6px;padding-top:16px}
.menu-btn{width:146px;height:16px;border-radius:2px;background:linear-gradient(var(--btn-top),var(--btn-bottom));color:var(--white);font-size:6.5px;font-weight:700;text-transform:uppercase;display:flex;align-items:center;justify-content:center;position:relative;box-shadow:0 1px 1px rgba(0,0,0,.4)}
.menu-btn::after{content:"";position:absolute;right:6px;top:5px;width:4px;height:4px;border-right:1.2px solid #fff;border-top:1.2px solid #fff;transform:rotate(45deg)}
.account .menu{padding-top:30px}

/* price button */
.price-btn{width:44px;border-radius:2px;overflow:hidden;flex:none}
.price-btn .amount{height:17px;background:linear-gradient(#ff3a3f,var(--red) 55%,var(--red-dark));color:var(--white);font-family:"Tinos",serif;font-size:12px;text-align:center;line-height:17px}
.price-btn .add{height:9px;background:#1e1e1e;color:#fff;font-size:3.6px;display:flex;align-items:center;justify-content:center;gap:2px;text-transform:uppercase}
.price-btn .add svg{width:7px;height:7px}

/* welcome */
.welcome-image{height:62px;background:var(--white);display:flex;align-items:center;justify-content:center;font-size:7px;color:#333;margin-top:10px}
.login-form{flex:1;display:flex;flex-direction:column;align-items:center;padding-top:7px;gap:7px}
.field{width:130px;height:15px;border:1px solid #888;border-radius:2px;background:#fff;font-size:7px;padding-left:4px;line-height:13px}
.login-btn{width:82px;height:16px;background:linear-gradient(var(--btn-top),var(--btn-bottom));color:#fff;font-size:7px;display:flex;align-items:center;justify-content:center;gap:3px;border-radius:2px;margin-top:2px}
.login-btn svg{width:7px;height:7px}
.help-links{height:17px;flex:none;background:var(--strip);display:flex;justify-content:space-between;align-items:center;padding:0 10px;font-size:5.5px;color:#333}
.create-account{height:30px;flex:none;background:linear-gradient(#4d4d50,#333336);color:#fff;font-size:7.5px;font-weight:700;display:flex;align-items:center;justify-content:center}

/* promotion */
.promo-card{position:absolute;left:9px;right:9px;top:6px;height:122px;background:var(--tan);border-radius:2px;padding:5px 6px}
.promo-card .name{text-align:center;font-size:7.5px;margin-bottom:4px}
.promo-card .photo{height:64px;background:var(--white)}
.promo-card .details{display:flex;justify-content:space-between;align-items:flex-start;margin-top:6px}
.promo-card .info{font-size:5.5px;line-height:7px}
.promo-card .info b{color:#1b2a6b}

/* product list */
.product-list{padding:6px 9px;display:flex;flex-direction:column;gap:5px}
.product-card{height:55px;background:var(--tan);border-radius:2px;display:flex;padding:4px;gap:6px}
.product-card .thumb{width:64px;height:44px;background:var(--white);flex:none}
.product-card .info{flex:1;font-size:5.3px;line-height:6.5px}
.product-card .pname{font-size:7px;border-bottom:1px solid var(--tan-line);margin-bottom:3px;padding-bottom:1px}
.product-card .row{display:flex;justify-content:space-between}
.product-card .view{font-weight:700}

/* basket */
.basket-list{position:absolute;left:10px;right:10px;top:6px;height:122px;background:var(--tan);border-radius:3px;padding:5px 8px}
.line-item{display:flex;justify-content:space-between;align-items:baseline;border-bottom:1px solid #8e8a80;height:15px;font-size:7px;padding-top:3px}
.line-item small{font-size:5px}
.line-item .price{font-size:5px}
.line-item .price span{font-family:"Tinos",serif;font-size:11px}
.basket-total{display:flex;justify-content:space-between;align-items:baseline;margin-top:4px;font-size:6px}
.basket-total b{font-size:6.5px}
.basket-total .sum{font-family:"Tinos",serif;font-size:13px}
.action-strip{position:absolute;left:0;right:0;bottom:0;height:18px;background:var(--strip);display:flex;justify-content:space-around;align-items:center;font-size:7.5px}

/* order form */
.order-sheet{position:absolute;left:10px;right:10px;top:5px;height:152px;background:var(--tan);border:1px solid var(--tan-line);border-radius:4px;padding:4px 3px}
.order-meta{text-align:center;font-size:4.5px;font-weight:700;margin-bottom:4px}
.order-paper{background:var(--white);padding:2px 3px;font-size:5.5px;line-height:7px}
.order-paper .rule{border-top:1px solid #777;margin:1px 0}
.order-paper .rule.tan{border-top:2px solid var(--tan-line)}
.order-row{display:flex;justify-content:space-between;padding-right:8px}
.order-row.head{font-weight:700}
.order-total{display:flex;justify-content:flex-end;align-items:baseline;gap:4px;margin-top:8px;padding-right:6px;font-size:7px}
.order-total span{font-family:"Tinos",serif;font-size:13px}
</style>
</head>
<body>

<svg class="icon-defs" aria-hidden="true">
  <defs>
    <symbol id="i-home" viewBox="0 0 16 16"><path d="M2 8 L8 2.5 L14 8 M4 7 V14 H7 V10 H9 V14 H12 V7" fill="none" stroke="currentColor" stroke-width="1.2"/></symbol>
    <symbol id="i-user" viewBox="0 0 16 16"><circle cx="8" cy="5.5" r="3" fill="none" stroke="currentColor" stroke-width="1.2"/><path d="M2.5 14.5 C3 10 13 10 13.5 14.5 Z" fill="none" stroke="currentColor" stroke-width="1.2"/></symbol>
    <symbol id="i-cart" viewBox="0 0 16 16"><path d="M1 3 H3.5 L5 11 H13 L14.5 5 H4" fill="none" stroke="currentColor" stroke-width="1.2"/><circle cx="6" cy="13.5" r="1.1" fill="currentColor"/><circle cx="12" cy="13.5" r="1.1" fill="currentColor"/></symbol>
    <symbol id="i-search" viewBox="0 0 16 16"><circle cx="7" cy="7" r="4.5" fill="none" stroke="currentColor" stroke-width="1.4"/><path d="M10.3 10.3 L14 14" stroke="currentColor" stroke-width="1.6"/></symbol>
    <symbol id="i-promo" viewBox="0 0 16 16"><path d="M8 1 L9.6 2.7 L12 2.3 L12.4 4.7 L14.5 6 L13.4 8 L14.5 10 L12.4 11.3 L12 13.7 L9.6 13.3 L8 15 L6.4 13.3 L4 13.7 L3.6 11.3 L1.5 10 L2.6 8 L1.5 6 L3.6 4.7 L4 2.3 L6.4 2.7 Z" fill="none" stroke="currentColor" stroke-width="1.1"/><path d="M8 5 V9" stroke="currentColor" stroke-width="1.4"/><circle cx="8" cy="11" r=".8" fill="currentColor"/></symbol>
    <symbol id="i-back" viewBox="0 0 16 16"><path d="M6 3 L2 7 L6 11 M2 7 H10 C13 7 14 9 14 14" fill="none" stroke="currentColor" stroke-width="1.3"/></symbol>
    <symbol id="i-logout" viewBox="0 0 16 16"><rect x="5" y="2" width="9" height="12" fill="none" stroke="currentColor" stroke-width="1.3"/><path d="M8 8 H1 M3.5 5.5 L1 8 L3.5 10.5" fill="none" stroke="currentColor" stroke-width="1.3"/></symbol>
    <symbol id="i-lock" viewBox="0 0 16 16"><rect x="3" y="7" width="10" height="8" fill="currentColor"/><path d="M5 7 V5 C5 1.5 11 1.5 11 5 V7" fill="none" stroke="currentColor" stroke-width="1.6"/></symbol>
  </defs>
</svg>

<!-- Welcome / log-in -->
<section class="screen welcome" style="left:69px;top:94px">
  <header class="app-header">
    <div class="brand">PANTRY</div>
  </header>
  <div class="title-bar">Welcome</div>
  <div class="welcome-image" role="img" aria-label="Welcome banner image">image</div>
  <form class="login-form">
    <div class="field">Username</div>
    <div class="field">Password</div>
    <div class="login-btn"><svg><use href="#i-lock"/></svg>LOGIN</div>
  </form>
  <div class="help-links"><span>Forget password?</span><span>Don't have an account?</span></div>
  <div class="create-account">Create New Account</div>
</section>

<!-- Homepage -->
<section class="screen" style="left:356px;top:94px">
  <header class="app-header">
    <div class="head-action back"><svg><use href="#i-back"/></svg>BACK</div>
    <div class="brand">PANTRY</div>
    <div class="head-action logout"><svg><use href="#i-logout"/></svg>LOG OUT</div>
  </header>
  <div class="title-bar">Homepage</div>
  <div class="search-band"><div class="search-field"><svg><use href="#i-search"/></svg>Search</div></div>
  <div class="content">
    <nav class="menu">
      <div class="menu-btn">Promotions</div>
      <div class="menu-btn">Catalogue</div>
      <div class="menu-btn">Basket</div>
      <div class="menu-btn">Order Template</div>
      <div class="menu-btn">Open Order</div>
      <div class="menu-btn">My Account</div>
    </nav>
  </div>
  <nav class="tab-bar">
    <div class="tab active"><svg><use href="#i-home"/></svg>Home page</div>
    <div class="tab"><svg><use href="#i-user"/></svg>My account</div>
    <div class="tab"><svg><use href="#i-cart"/></svg>My basket</div>
    <div class="tab"><svg><use href="#i-search"/></svg>Products</div>
    <div class="tab"><svg><use href="#i-promo"/></svg>Promo</div>
  </nav>
</section>

<!-- Promotion -->
<section class="screen" style="left:645px;top:94px">
  <header class="app-header">
    <div class="head-action back"><svg><use href="#i-back"/></svg>BACK</div>
    <div class="brand">PANTRY</div>
    <div class="head-action logout"><svg><use href="#i-logout"/></svg>LOG OUT</div>
  </header>
  <div class="title-bar">Promotion page</div>
  <div class="search-band"><div class="search-field"><svg><use href="#i-search"/></svg>Search</div></div>
  <div class="content">
    <article class="promo-card">
      <div class="name">Product name</div>
      <div class="photo" role="img" aria-label="Promoted product photo"></div>
      <div class="details">
        <div class="info">Product Information...<br><b>Package:</b> 1 box x 12 pcs<br>Dimensions: 180/250mm</div>
        <div class="price-btn"><div class="amount">$ 60</div><div class="add"><svg><use href="#i-cart"/></svg>Add to basket</div></div>
      </div>
    </article>
  </div>
  <nav class="tab-bar">
    <div class="tab"><svg><use href="#i-home"/></svg>Home page</div>
    <div class="tab"><svg><use href="#i-user"/></svg>My account</div>
    <div class="tab"><svg><use href="#i-cart"/></svg>My basket</div>
    <div class="tab"><svg><use href="#i-search"/></svg>Products</div>
    <div class="tab active"><svg><use href="#i-promo"/></svg>Promo</div>
  </nav>
</section>

<!-- Products -->
<section class="screen" style="left:933px;top:94px">
  <header class="app-header">
    <div class="head-action back"><svg><use href="#i-back"/></svg>BACK</div>
    <div class="brand">PANTRY</div>
    <div class="head-action logout"><svg><use href="#i-logout"/></svg>LOG OUT</div>
  </header>
  <div class="title-bar">Products</div>
  <div class="search-band"><div class="search-field"><svg><use href="#i-search"/></svg>Search</div></div>
  <div class="content">
    <div class="product-list">
      <article class="product-card">
        <div class="thumb" role="img" aria-label="Product photo"></div>
        <div class="info"><div class="pname">Product name</div>
          <div class="row"><div><span class="view">view details</span><br>1 box x 12 pcs<br>180/250mm</div>
          <div class="price-btn"><div class="amount">$ 60</div><div class="add"><svg><use href="#i-cart"/></svg>Add to basket</div></div></div>
        </div>
      </article>
      <article class="product-card">
        <div class="thumb" role="img" aria-label="Product photo"></div>
        <div class="info"><div class="pname">Product name</div>
          <div class="row"><div><span class="view">view details</span><br>1 box x 12 pcs<br>180/250mm</div>
          <div class="price-btn"><div class="amount">$ 60</div><div class="add"><svg><use href="#i-cart"/></svg>Add to basket</div></div></div>
        </div>
      </article>
      <article class="product-card">
        <div class="thumb" role="img" aria-label="Product photo"></div>
        <div class="info"><div class="pname">Product name</div>
          <div class="row"><div><span class="view">view details</span><br>1 box x 12 pcs<br>180/250mm</div>
          <div class="price-btn"><div class="amount">$ 60</div><div class="add"><svg><use href="#i-cart"/></svg>Add to basket</div></div></div>
        </div>
      </article>
    </div>
  </div>
  <nav class="tab-bar">
    <div class="tab"><svg><use href="#i-home"/></svg>Home page</div>
    <div class="tab"><svg><use href="#i-user"/></svg>My account</div>
    <div class="tab"><svg><use href="#i-cart"/></svg>My basket</div>
    <div class="tab active"><svg><use href="#i-search"/></svg>Products</div>
    <div class="tab"><svg><use href="#i-promo"/></svg>Promo</div>
  </nav>
</section>

<!-- My basket -->
<section class="screen" style="left:69px;top:496px">
  <header class="app-header">
    <div class="head-action back"><svg><use href="#i-back"/></svg>BACK</div>
    <div class="brand">PANTRY</div>
    <div class="head-action logout"><svg><use href="#i-logout"/></svg>LOG OUT</div>
  </header>
  <div class="title-bar">My basket</div>
  <div class="search-band"><div class="search-field"><svg><use href="#i-search"/></svg>Search</div></div>
  <div class="content">
    <div class="basket-list">
      <div class="line-item"><span>Apple - 2 <small>kg</small></span><span class="price">Price <span>$ 3</span></span></div>
      <div class="line-item"><span>Tomatoes - 4 <small>kg</small></span><span class="price">Price <span>$ 7</span></span></div>
      <div class="line-item"><span>Apple - 2 <small>kg</small></span><span class="price">Price <span>$ 3</span></span></div>
      <div class="line-item"><span>Tomatoes - 4 <small>kg</small></span><span class="price">Price <span>$ 7</span></span></div>
      <div class="line-item"><span>Pears - 2 <small>kg</small></span><span class="price">Price <span>$ 8</span></span></div>
      <div class="line-item"><span>Peach - 1 <small>kg</small></span><span class="price">Price <span>$ 2</span></span></div>
      <div class="basket-total"><b>TOTAL</b><span>5 Iteams</span><span class="sum">$ 23</span></div>
    </div>
    <div class="action-strip"><span>NEW LIST</span><span>REMOVE</span></div>
  </div>
  <nav class="tab-bar">
    <div class="tab"><svg><use href="#i-home"/></svg>Home page</div>
    <div class="tab"><svg><use href="#i-user"/></svg>My account</div>
    <div class="tab active"><svg><use href="#i-cart"/></svg>My basket</div>
    <div class="tab"><svg><use href="#i-search"/></svg>Products</div>
    <div class="tab"><svg><use href="#i-promo"/></svg>Promo</div>
  </nav>
</section>

<!-- My account -->
<section class="screen account" style="left:356px;top:496px">
  <header class="app-header">
    <div class="head-action back"><svg><use href="#i-back"/></svg>BACK</div>
    <div class="brand">PANTRY</div>
    <div class="head-action logout"><svg><use href="#i-logout"/></svg>LOG OUT</div>
  </header>
  <div class="title-bar">My account</div>
  <div class="search-band"><div class="search-field"><svg><use href="#i-search"/></svg>Search</div></div>
  <div class="content">
    <nav class="menu">
      <div class="menu-btn">Check Account</div>
      <div class="menu-btn">Check Order</div>
      <div class="menu-btn">Check Recent</div>
      <div class="menu-btn">Past Order</div>
      <div class="menu-btn">More Details</div>
    </nav>
  </div>
  <nav class="tab-bar">
    <div class="tab"><svg><use href="#i-home"/></svg>Home page</div>
    <div class="tab active"><svg><use href="#i-user"/></svg>My account</div>
    <div class="tab"><svg><use href="#i-cart"/></svg>My basket</div>
    <div class="tab"><svg><use href="#i-search"/></svg>Products</div>
    <div class="tab"><svg><use href="#i-promo"/></svg>Promo</div>
  </nav>
</section>

<!-- Order template -->
<section class="screen" style="left:645px;top:496px">
  <header class="app-header">
    <div class="head-action back"><svg><use href="#i-back"/></svg>BACK</div>
    <div class="brand">PANTRY</div>
    <div class="head-action logout"><svg><use href="#i-logout"/></svg>LOG OUT</div>
  </header>
  <div class="title-bar">Order template</div>
  <div class="content">
    <div class="order-sheet">
      <div class="order-meta">Date 12.01.2013 &nbsp; Client Code:</div>
      <div class="order-paper">
        <div>Name:</div><div class="rule"></div>
        <div>Company:</div><div>Address:</div><div>Phone:</div>
        <div class="rule tan"></div>
        <div class="order-row head"><span>Iteam name</span><span>Price</span></div>
        <div class="order-row"><span>1. Products</span><span>$12</span></div>
        <div class="order-row"><span>2. Products</span><span>$11</span></div>
        <div>3. Products</div><div>4. Products</div><div>5. Products</div>
      </div>
      <div class="order-total">TOTAL <span>$ 23</span></div>
    </div>
    <div class="action-strip"><span>NEW LIST</span><span>REMOVE</span></div>
  </div>
  <nav class="tab-bar">
    <div class="tab"><svg><use href="#i-home"/></svg>Home page</div>
    <div class="tab"><svg><use href="#i-user"/></svg>My account</div>
    <div class="tab"><svg><use href="#i-cart"/></svg>My basket</div>
    <div class="tab"><svg><use href="#i-search"/></svg>Products</div>
    <div class="tab"><svg><use href="#i-promo"/></svg>Promo</div>
  </nav>
</section>

<!-- Order -->
<section class="screen" style="left:933px;top:496px">
  <header class="app-header">
    <div class="head-action back"><svg><use href="#i-back"/></svg>BACK</div>
    <div class="brand">PANTRY</div>
    <div class="head-action logout"><svg><use href="#i-logout"/></svg>LOG OUT</div>
  </header>
  <div class="title-bar">Order</div>
  <div class="content">
    <div class="order-sheet">
      <div class="order-meta">Date 12.01.2013 &nbsp; Client Code:</div>
      <div class="order-paper">
        <div>Name:</div><div class="rule"></div>
        <div>Company:</div><div>Address:</div><div>Phone:</div>
        <div class="rule tan"></div>
        <div class="order-row head"><span>Iteam name</span><span>Price</span></div>
        <div class="order-row"><span>1. Products</span><span>$12</span></div>
        <div class="order-row"><span>2. Products</span><span>$11</span></div>
        <div>3. Products</div><div>4. Products</div><div>5. Products</div>
      </div>
      <div class="order-total">TOTAL <span>$ 23</span></div>
    </div>
  </div>
  <nav class="tab-bar">
    <div class="tab"><svg><use href="#i-home"/></svg>Home page</div>
    <div class="tab"><svg><use href="#i-user"/></svg>My account</div>
    <div class="tab"><svg><use href="#i-cart"/></svg>My basket</div>
    <div class="tab"><svg><use href="#i-search"/></svg>Products</div>
    <div class="tab"><svg><use href="#i-promo"/></svg>Promo</div>
  </nav>
</section>

</body>
</html>
```